Business Card for Business consulting practice

Need a design for a consultant business card. Simple and elegant.
I need the following information on the card:
Logo: (see uploaded file)
Company name: Calmora Advisory Group
Name: Dana Weltrup
Title: Managing Director - Aerospace and Defence
Phone #: 514-268-3917
e-mail: dana.weltrup@calmora-example.com
Website: www.calmora-example.com
Tagline: Proposals Management and Capture support for complex procurements

```html
<!DOCTYPE html>
<html lang="en">
<head>
<meta charset="utf-8">
<title>Calmora Advisory Group – Business Card</title>
<link rel="stylesheet" href="https://fonts.googleapis.com/css2?family=Open+Sans:wght@400;600&display=swap">
<style>
  :root {
    --navy: #0f2c44;
    --navy-back: #12304a;
    --accent: #1f8fc0;
    --white: #ffffff;
    --stage: #7a848c;
    --text-font: "Open Sans", Arial, sans-serif;
  }
  * { box-sizing: border-box; margin: 0; padding: 0; }
  html, body {
    width: 1200px; height: 807px; overflow: hidden;
    background: var(--stage);
    font-family: var(--text-font);
  }
  .canvas { position: relative; width: 1200px; height: 807px; }
  .card {
    position: absolute; left: 342px; width: 516px; height: 294px;
    overflow: hidden;
    box-shadow: 0 3px 8px rgba(0,0,0,0.35);
  }
  .card--front { top: 82px; background: var(--white); }
  .card--back { top: 430px; background: var(--navy-back); }
  .card__waves { position: absolute; inset: 0; }
  .wordmark {
    position: absolute; left: 0; right: 0; text-align: center;
    font-weight: 600; font-size: 23px; letter-spacing: 2.5px;
    text-transform: uppercase; white-space: nowrap;
  }
  .card--front .wordmark { top: 36px; color: var(--navy); }
  .card--back .wordmark { top: 108px; color: var(--white); }
  .holder {
    position: absolute; left: 0; right: 0; text-align: center;
    color: var(--white); text-transform: uppercase; white-space: nowrap;
  }
  .holder__name { top: 164px; font-size: 21px; letter-spacing: 1.2px; }
  .holder__title { top: 200px; font-size: 14px; letter-spacing: 1px; }
  .contact-rule {
    position: absolute; left: 8px; width: 480px; top: 234px;
    height: 1px; background: var(--accent);
  }
  .contacts {
    position: absolute; left: 8px; width: 482px; top: 256px;
    display: flex; align-items: center; justify-content: space-between;
    color: var(--white); font-size: 9.6px; letter-spacing: 0.1px;
    text-transform: uppercase; white-space: nowrap;
  }
  .contacts__sep {
    display: inline-block; width: 1px; height: 16px;
    background: var(--accent);
  }
  .tagline {
    position: absolute; left: 0; right: 0; top: 226px; text-align: center;
    color: var(--white); font-size: 12.5px; letter-spacing: 2.6px;
    line-height: 22px; text-transform: uppercase;
  }
</style>
</head>
<body>
<main class="canvas">
  <section class="card card--front" aria-label="Business card front">
    <svg class="card__waves" width="516" height="294" viewBox="0 0 516 294" aria-hidden="true">
      <path d="M0 120 H360 C455 120 512 172 516 294 H0 Z" fill="var(--accent)"/>
      <path d="M0 134 H352 C440 134 494 182 500 294 H0 Z" fill="var(--navy)"/>
    </svg>
    <div class="wordmark">Calmora Advisory Group</div>
    <div class="holder holder__name">Dana Weltrup</div>
    <div class="holder holder__title">Managing Director - Aerospace and Defence</div>
    <div class="contact-rule"></div>
    <div class="contacts">
      <span>514-268-3917</span>
      <span class="contacts__sep"></span>
      <span>www.calmora-example.com</span>
      <span class="contacts__sep"></span>
      <span>dana.weltrup@calmora-example.com</span>
    </div>
  </section>

  <section class="card card--back" role="img" aria-label="Business card back: navy background with faint repeated brand pattern">
    <div class="wordmark">Calmora Advisory Group</div>
    <p class="tagline">Proposals management and capture support<br>for complex procurements</p>
  </section>
</main>
</body>
</html>
```